Business Card - high end, modern health care

Hey designers!

We need a double sided business card for the boutique, cutting edge physical therapy rehabilitation centre in Sydney's Northern Beaches.

With the most qualified physios in the area The Harbourline Motion Clinic does what other physiotherapy practices do not, we take our time with our patients giving them longer appointments, better physios and therefor faster results!

We guarantee that the service people receive at THMC will be unparalleled.

Hence we need a business card to reflect our modern, boutique, high end service. The final design needs to reflect that we are in a class of our own yet with the feel of beachside retreat.

Below I have attached our logo in both blue on white and white on blue. The exact colour is;
and the font that we have used in our logo is Tex Gyre Aventador.

I like the idea of the blue as the main colour as it is more eye catching and our signage onto the main road will be in this blue and in the interest of consistency across marketing the blue needs to be a part of the design. However I would appreciate a few designs onto a wooden background as this is a visual theme within the fitout of the practice.

The design needs to be of standard size (91x55mm).

Target Market(s)

We target people who have an end outcome in mind and those who have had poor experiences with other providers and ensure that everyone gets the care that they deserve with a premium service that is tailored to the individuals circumstances. As a premium service, the target market is highly educated, business and tech savvy with the additional target market of elderly people who have self funded their retirement and see value in paying for the best ongoing rehabilitation to maintain independence.

Industry/Entity Type

Physical Therapy

Contact Information for Business Card

Name, designation( Titled Musculoskeletal Physiotherapist... there will also be those in the company that have multiple designations ie 5 or 6 words long), phone number, email, facebook, instagram, address

Font styles to use
Sans Serif

Colors

Designer to choose colors to be used in the design.

Requirements
Must have
• Front - The logo as large as possible, blue or wooden theme, and all of the important details.
• Back - A blank space/lines on which to write appointment times (no "Appointment, date, time" etc.)
Nice to have
• facebook url
• logos for facebook and instagram
• Mini logos for the phone and email?

```html
<!DOCTYPE html>
<html lang="en">
<head>
<meta charset="utf-8">
<title>The Harbourline Motion Clinic – Business Card</title>
<link rel="stylesheet" href="https://fonts.googleapis.com/css2?family=Montserrat:wght@400;500;700&display=swap">
<style>
  :root {
    --page-bg: #e4e6ea;
    --card-paper: #f3f3f1;
    --brand-blue: #1d63b8;
    --brand-blue-deep: #1247b8;
    --brand-blue-bright: #2a7ae6;
    --white: #ffffff;
  }
  * { box-sizing: border-box; margin: 0; padding: 0; }
  html, body {
    width: 1200px; height: 900px; overflow: hidden;
    background: var(--page-bg);
    font-family: "Montserrat", Arial, sans-serif;
  }
  .stage {
    width: 1200px; height: 900px;
    display: flex; justify-content: center; align-items: center; gap: 60px;
  }
  .card {
    width: 435px; height: 720px; flex-shrink: 0;
    box-shadow: 0 12px 30px rgba(0,0,0,.18);
    display: flex; flex-direction: column; align-items: center;
    position: relative; overflow: hidden;
  }
  .card > * { flex-shrink: 0; }

  /* Front */
  .card--front { background: var(--card-paper); color: var(--brand-blue); padding-top: 52px; }
  .holder-name { font-weight: 700; font-size: 27px; line-height: 1.2; letter-spacing: .5px; }
  .holder-role { font-weight: 500; font-size: 18px; line-height: 1.2; margin-top: 2px; }
  .divider { width: 24px; height: 3px; background: currentColor; margin: 16px 0; }
  .brand-disc {
    width: 250px; height: 250px; border-radius: 50%;
    background: var(--brand-blue); flex-shrink: 0;
  }
  .brand-name {
    font-weight: 700; font-size: 25px; line-height: 1.15; text-align: center;
    letter-spacing: 1px; margin-top: 22px; text-transform: uppercase;
  }
  .contact-icons { display: flex; gap: 22px; margin-top: 26px; }
  .contact-icon {
    width: 30px; height: 30px; border-radius: 50%; background: var(--brand-blue);
    display: flex; align-items: center; justify-content: center;
  }
  .contact-lines { margin-top: 16px; text-align: center; font-size: 19px; line-height: 1.7; font-weight: 500; }

  /* Back */
  .card--back {
    background: linear-gradient(160deg, var(--brand-blue-bright) 0%, var(--brand-blue-deep) 100%);
    color: var(--white); padding-top: 96px;
  }
  .card--back .brand-disc { background: var(--white); width: 270px; height: 270px; }
  .card--back .brand-name { color: var(--white); margin-top: 28px; }
  .card--back .divider { margin: 18px 0 26px; }
  .appointment-fields { width: 330px; display: flex; flex-direction: column; gap: 16px; }
  .appointment-field { height: 34px; background: var(--white); }
</style>
</head>
<body>
<main class="stage">
  <section class="card card--front">
    <h1 class="holder-name">DANIEL REEVE</h1>
    <p class="holder-role">Senior Physiotherapist</p>
    <span class="divider"></span>
    <div class="brand-disc" role="img" aria-label="Clinic emblem area"></div>
    <p class="brand-name">The Harbourline<br>Motion Clinic</p>
    <div class="contact-icons">
      <span class="contact-icon">
        <svg width="16" height="16" viewBox="0 0 24 24" aria-label="Phone"><path fill="#fff" d="M6.6 10.8a15.1 15.1 0 0 0 6.6 6.6l2.2-2.2c.3-.3.7-.4 1-.2 1.1.4 2.3.6 3.6.6.6 0 1 .4 1 1V20c0 .6-.4 1-1 1A17 17 0 0 1 3 4c0-.6.4-1 1-1h3.5c.6 0 1 .4 1 1 0 1.3.2 2.5.6 3.6.1.3 0 .7-.2 1z"/></svg>
      </span>
      <span class="contact-icon">
        <svg width="16" height="16" viewBox="0 0 24 24" aria-label="Email"><rect x="3" y="5" width="18" height="14" rx="2" fill="#fff"/><path d="M3.5 6.5 12 13l8.5-6.5" stroke="#1d63b8" stroke-width="1.8" fill="none"/></svg>
      </span>
      <span class="contact-icon" aria-label="Social profile"></span>
      <span class="contact-icon" aria-label="Social profile"></span>
    </div>
    <div class="contact-lines">
      <p>0061 402 318</p>
      <p>hello@harbourlinemotion.com.au</p>
      <p>harbourlinemotionclinic</p>
    </div>
    <span class="divider"></span>
  </section>

  <section class="card card--back">
    <div class="brand-disc" role="img" aria-label="Clinic emblem area"></div>
    <p class="brand-name">The Harbourline<br>Motion Clinic</p>
    <span class="divider"></span>
    <div class="appointment-fields">
      <div class="appointment-field"></div>
      <div class="appointment-field"></div>
      <div class="appointment-field"></div>
    </div>
  </section>
</main>
</body>
</html>
```